Bidmo Store Banner

I have an bidmo store which displays the store name which is Mrs.Wexley's Drifting Moon-Bazaar. I want to make this store landing page look better so I want a design to be used as what bidmo calls a Store banner. I attach a pic of the visuals of the landing page of my store and I also attach a pic of another store who have set up a banner.

Colors
85cae6
6cbee2
33a6d7
0355a3
3276b5
cedeed
d6edf3
eaf1f7

```html
<!DOCTYPE html>
<html lang="en">
<head>
<meta charset="utf-8">
<title>Mrs. Wexley's Moon Bazaar – Store Banner</title>
<link rel="stylesheet" href="https://fonts.googleapis.com/css2?family=Courgette&display=swap">
<style>
  :root {
    --sky: #62b7e6;
    --sky-light: #85cae6;
    --sky-wave: #6cbee2;
    --banner-blue: #1f6aa0;
    --portrait-scarf: #b5432e;
    --portrait-hair: #e6c27e;
    --portrait-skin: #f0cfae;
    --portrait-dark: #2e2424;
    --sign-red: #b5432e;
    --sign-gold: #f2ad2c;
    --white: #ffffff;
  }
  * { margin: 0; padding: 0; box-sizing: border-box; }
  html, body { width: 1200px; height: 270px; overflow: hidden; background: var(--sky); }
  .store-banner {
    position: relative;
    width: 1200px;
    height: 270px;
    overflow: hidden;
    background: var(--sky);
    font-family: "Courgette", cursive;
  }
  .store-banner__waves { position: absolute; inset: 0; }

  .store-banner__portrait {
    position: absolute;
    left: 8px;
    top: 6px;
    width: 250px;
    height: 270px;
    border-radius: 125px 125px 0 0;
    background: linear-gradient(180deg,
      var(--portrait-scarf) 0%,
      var(--portrait-scarf) 14%,
      var(--portrait-hair) 30%,
      var(--portrait-skin) 55%,
      var(--portrait-hair) 75%,
      var(--portrait-dark) 100%);
  }

  .store-banner__title-plate {
    position: absolute;
    left: 248px;
    top: 44px;
    width: 530px;
    height: 170px;
  }
  .store-banner__title {
    position: absolute;
    left: 262px;
    top: 56px;
    width: 500px;
    color: var(--white);
    text-align: center;
    font-weight: 400;
    line-height: 1;
  }
  .store-banner__title-line { display: block; font-size: 58px; letter-spacing: 1px; }
  .store-banner__title-line--second { padding-top: 22px; padding-right: 24px; }

  .store-mark {
    position: absolute;
    left: 800px;
    top: 40px;
    width: 380px;
    height: 190px;
    display: flex;
    align-items: center;
    justify-content: center;
    gap: 16px;
  }
  .store-mark__name {
    font-size: 44px;
    line-height: 1.15;
    text-align: center;
    color: var(--sign-red);
  }
  .store-mark__dot {
    flex: none;
    width: 34px;
    height: 34px;
    border-radius: 50%;
    background: var(--sign-gold);
  }
</style>
</head>
<body>
  <header class="store-banner">
    <svg class="store-banner__waves" width="1200" height="270" viewBox="0 0 1200 270" aria-hidden="true">
      <path d="M0 70 C 200 20, 380 120, 600 60 S 980 10, 1200 70 L1200 110 C 980 60, 800 140, 600 100 S 200 70, 0 120 Z" fill="var(--sky-wave)" opacity="0.55"/>
      <path d="M0 210 C 240 170, 420 250, 640 200 S 1000 160, 1200 220 L1200 270 L0 270 Z" fill="var(--sky-light)" opacity="0.35"/>
    </svg>

    <div class="store-banner__portrait" role="img" aria-label="Cartoon portrait of the shop owner with blonde hair, glasses and a red head scarf"></div>

    <svg class="store-banner__title-plate" viewBox="0 0 530 170" aria-hidden="true">
      <polygon points="0,2 528,52 518,140 14,168" fill="var(--banner-blue)"/>
    </svg>

    <h1 class="store-banner__title">
      <span class="store-banner__title-line">Mrs. Wexley’s</span>
      <span class="store-banner__title-line store-banner__title-line--second">Moon Bazaar</span>
    </h1>

    <div class="store-mark">
      <span class="store-mark__name">Mrs. Wexley’s<br>Moon Bazaar</span>
      <span class="store-mark__dot"></span>
    </div>
  </header>
</body>
</html>
```